Brightway Rug and Floor cleaning Business card Design

I need a design that has the same feel as my van.
i would also like a prominent "Review us on facebook" somewhere, but not that it makes it look silly.
I would like the card to have a little bit of grey or black in the design as well.

It will need contact details
phone: 0498 276154
email: rkbrightwayfloors@mailbox-example.com
website: www.brightwayrugandfloorcleaning-example.com.au
facebook: /brightwayrugandfloorcleaning

Industry/Entity Type

Business

Contact Information for Business Card

Phone number 0498276154
Email rkbrightwayfloors@mailbox-example.com
Website www.brightwayrugandfloorcleaning-example.com.au
Facebook/brightwayrugandfloorcleaning

Colors
000000

Requirements
Must have
• Same feel as my van
• I want the card to stand out from the crowd
Nice to have
• Maybe include a tiny bit of a third colour? Grey's,blacks, orange?

```html
<!DOCTYPE html>
<html lang="en">
<head>
<meta charset="utf-8">
<title>Brightway Rug and Floor cleaning – Business Card</title>
<link rel="stylesheet" href="https://fonts.googleapis.com/css2?family=Source+Sans+3:wght@400;600;700&display=swap">
<style>
  :root {
    --page-bg: #e6e4e1;
    --card-white: #f4f4f5;
    --card-white-edge: #e3e4e6;
    --card-black: #1c1c1c;
    --arc-dark: #2c2c2c;
    --arc-mid: #3a3a3a;
    --ink-dark: #2a2a2a;
    --ink-grey: #6e6e6e;
    --logo-white: #f1f1f1;
  }
  * { box-sizing: border-box; margin: 0; padding: 0; }
  html, body {
    width: 1200px; height: 1023px; overflow: hidden;
    background: var(--page-bg);
    font-family: "Source Sans 3", "Myriad Pro", sans-serif;
  }
  .card {
    position: absolute; left: 250px; width: 700px; height: 400px;
    box-shadow: 0 4px 18px rgba(0,0,0,0.18);
    overflow: hidden;
  }
  .card-front {
    top: 70px;
    background: linear-gradient(160deg, var(--card-white) 0%, var(--card-white-edge) 100%);
  }
  .card-back { top: 550px; background: var(--card-black); }

  .review-line {
    position: absolute; left: 50px; top: 48px;
    font-size: 26px; font-weight: 400; color: var(--ink-dark);
    letter-spacing: 0.2px;
  }
  .review-line strong { font-weight: 700; }

  .contact-list {
    position: absolute; left: 50px; bottom: 44px;
    display: grid; grid-template-columns: auto 1fr;
    column-gap: 10px; row-gap: 4px;
    font-size: 19px; line-height: 1.2;
  }
  .contact-label { color: var(--ink-dark); font-weight: 600; }
  .contact-value { color: var(--ink-grey); }

  .back-art { position: absolute; inset: 0; }
  .brand-mark {
    position: absolute; left: 60px; top: 150px;
    display: flex; align-items: center; gap: 18px;
  }
  .brand-circle {
    width: 100px; height: 100px; border-radius: 50%;
    background: var(--logo-white); flex: none;
  }
  .brand-name {
    font-size: 28px; font-weight: 600; color: var(--logo-white);
  }
</style>
</head>
<body>
  <section class="card card-front" aria-label="Business card front">
    <p class="review-line">Review Us On <strong>Linkora!</strong></p>
    <dl class="contact-list">
      <dt class="contact-label">Linkora</dt><dd class="contact-value">brightwayrugandfloorcleaning</dd>
      <dt class="contact-label">Phone</dt><dd class="contact-value">0498276154</dd>
      <dt class="contact-label">Email</dt><dd class="contact-value">rkbrightwayfloors@mailbox-example.com</dd>
      <dt class="contact-label">Website</dt><dd class="contact-value">www.brightwayrugandfloorcleaning-example.com</dd>
    </dl>
  </section>

  <section class="card card-back" aria-label="Business card back">
    <svg class="back-art" width="700" height="400" viewBox="0 0 700 400" aria-hidden="true">
      <path d="M0 0 H150 Q90 200 150 400 H0 Z" fill="var(--arc-dark)"/>
      <path d="M150 0 H200 Q140 200 200 400 H150 Q90 200 150 0 Z" fill="var(--arc-mid)"/>
      <path d="M560 400 Q610 300 700 270 V400 Z" fill="var(--arc-dark)"/>
      <path d="M610 400 Q640 330 700 310 V400 Z" fill="var(--arc-mid)"/>
    </svg>
    <div class="brand-mark">
      <span class="brand-circle"></span>
      <span class="brand-name">Brightway Rug and Floor cleaning</span>
    </div>
  </section>
</body>
</html>
```